New to ArtHarbor? This Contest is for you!

Are you new to ArtHarbor and looking to enter your first contest? Look no further! We're launching this special contest to help you get started on building a design portfolio at ArtHarbor!

Requirements:
* Create a beautiful and eye-catching graphic design which includes the words "Spot me at ArtHarbor!"
* Upload your design to this contest AND share it on Chatterly
* You must upload your entry before 12:00am 1 April
* This must be your very FIRST entry on ArtHarbor to be eligible to receive a prize. If you've already entered other ArtHarbor contests you won't be eligible to win the prizes
* Your design must adhere to our quality standards to be eligible to receive a prize

Prizes:
* There are 150 x $5 participation payments ($750) available to be awarded to high-quality designs
* First prize for the best design is $150
* Second prize is $100

Requirements
Must have
• Your design must contain the words "Spot me at ArtHarbor".
• This must be your first entry on ArtHarbor to be eligible for the prizes.
• Your design must adhere to our quality standards.
Should not have
• No stock images or overused concepts.

```html
<!DOCTYPE html>
<html lang="en">
<head>
<meta charset="utf-8">
<title>Rayan Malik — Portfolio</title>
<link rel="stylesheet" href="https://fonts.googleapis.com/css2?family=Great+Vibes&family=Quicksand:wght@400;500;600;700&display=swap">
<style>
:root{
  --ink:#1f1f1f;
  --text:#555555;
  --muted:#8a8a8a;
  --white:#ffffff;
  --sand:#f2efe8;
  --accent:#d8262e;
  --pink:#e0147a;
  --dark-pill:#22231c;
  --social:#7a7a7a;
  --icon-tile:#2f2f2f;
}
*{box-sizing:border-box;margin:0;padding:0}
html,body{width:1200px;height:3178px;overflow:hidden}
body{position:relative;background:var(--white);font-family:'Quicksand',sans-serif;color:var(--text)}
.abs{position:absolute}

/* Hero */
.hero{left:0;top:0;width:1200px;height:755px;overflow:hidden}
.hero-photo{position:absolute;inset:0;background:radial-gradient(ellipse at 50% 30%,#5a5f63 0%,#3c4043 55%,#26292b 100%)}
.brand-mark{left:203px;top:32px;width:40px;height:40px;border:2px solid var(--white);border-radius:4px;background:rgba(255,255,255,.12)}
.main-nav{left:356px;top:35px;display:flex;gap:36px;font-size:14px;font-weight:500;color:#d9d9d9}
.main-nav .current{color:var(--white);font-weight:700}
.hero-name{left:0;top:62px;width:1200px;text-align:center;font-family:'Great Vibes',cursive;font-size:128px;font-weight:400;color:var(--white);line-height:1.2}
.hero-cta{left:416px;top:481px;width:370px;height:70px;border:2px solid var(--white);color:var(--white);font-size:24px;font-weight:600;display:flex;align-items:center;justify-content:center;letter-spacing:.5px}

/* Section titles */
.section-title{left:0;width:1200px;text-align:center;font-size:42px;font-weight:600;color:var(--ink);letter-spacing:1px;line-height:52px}
.section-title::after{content:"";display:block;width:150px;height:2px;background:var(--ink);margin:6px auto 0}

/* About */
.about-copy{left:250px;top:862px;width:700px;text-align:center;font-size:18px;line-height:24px;color:var(--text)}

/* Experience */
.band{left:0;width:1200px;background:var(--sand)}
.timeline-line{left:589px;top:1115px;width:6px;height:690px;background:var(--white)}
.timeline-node{width:44px;height:44px;border-radius:50%;background:var(--white);display:flex;align-items:center;justify-content:center}
.job-card{width:380px;height:112px;background:var(--white);padding:28px 32px}
.job-title{font-size:27px;color:var(--ink);font-weight:500;white-space:nowrap}
.job-role{font-size:18px;color:var(--text);margin-top:10px;white-space:nowrap}
.job-date{font-size:13px;color:var(--muted)}

/* Software */
.tool{width:74px;height:74px;background:var(--icon-tile);border:3px solid #9c9c9c;display:flex;align-items:center;justify-content:center;font-size:11px;font-weight:600;color:#cfcfcf}

/* Work */
.work-shot{overflow:hidden}
.work-tag{position:absolute;left:8px;top:8px;background:var(--accent);color:var(--white);font-size:20px;padding:3px 14px}
.work-card{background:var(--white)}
.work-card-title{position:absolute;left:20px;top:20px;font-size:20px;color:var(--ink)}
.work-card-meta{position:absolute;left:20px;top:50px;font-size:17px;color:var(--text)}
.work-card-meta span{color:var(--accent)}
.work-details{position:absolute;left:188px;top:205px;width:120px;height:36px;border:1px solid #444;font-size:14px;letter-spacing:2px;display:flex;align-items:center;justify-content:center;color:#444}

/* Contacts */
.contact-line{left:0;width:1200px;text-align:center;font-size:24px;color:var(--muted)}
.email-pill{left:452px;top:2870px;width:296px;height:44px;border-radius:14px;background:var(--dark-pill);color:var(--white);font-size:18px;display:flex;align-items:center;justify-content:center}
.social{width:86px;height:86px;border-radius:50%;background:var(--social);color:var(--white);font-size:14px;font-weight:600;display:flex;align-items:center;justify-content:center}
.footer-strip{left:0;top:3150px;width:1200px;height:28px;background:var(--sand);text-align:center;font-size:12px;color:var(--muted);line-height:28px}
</style>
</head>
<body>

<header class="abs hero">
  <div class="hero-photo" role="img" aria-label="Top-down photo of a dark desk with monitor, tablet, keyboard, mouse, glasses and notebooks"></div>
  <div class="abs brand-mark" aria-hidden="true"></div>
  <nav class="abs main-nav">
    <span class="current">Home</span><span>About</span><span>Portfolio</span><span>Services</span><span>Blog</span><span>Contact</span>
  </nav>
  <h1 class="abs hero-name">Rayan Malik</h1>
  <div class="abs hero-cta">Spot me at ArtHarbor!</div>
</header>

<section>
  <h2 class="abs section-title" style="top:775px">ABOUT</h2>
  <p class="abs about-copy">My name is Rayan, a Web &amp; App developer and designer currently based in Pakistan.<br>The combination of my coding skills and my designer eyes make it possible for me to satisfy clients with complete solution.</p>
</section>

<section class="abs band" style="top:997px;height:808px"></section>
<h2 class="abs section-title" style="top:1022px">Experience</h2>
<div class="abs timeline-line"></div>

<div class="abs job-card" style="left:163px;top:1128px"><div class="job-title">Quillon Tech</div><div class="job-role">Web &amp; Graphics Designer</div></div>
<div class="abs timeline-node" style="left:570px;top:1137px"><svg width="22" height="22" viewBox="0 0 22 22"><path d="M4 18 L16 6 M4 4 L18 18" stroke="#111" stroke-width="3"/><rect x="13" y="2" width="7" height="5" fill="#111" transform="rotate(45 16 4)"/></svg></div>
<div class="abs job-date" style="left:650px;top:1150px">2013-present</div>

<div class="abs job-card" style="left:648px;top:1275px"><div class="job-title">Merrowdale Studio</div><div class="job-role">Graphics Designer</div></div>
<div class="abs timeline-node" style="left:570px;top:1284px"><svg width="22" height="22" viewBox="0 0 22 22"><path d="M4 18 L16 6 M4 4 L18 18" stroke="#111" stroke-width="3"/><rect x="13" y="2" width="7" height="5" fill="#111" transform="rotate(45 16 4)"/></svg></div>
<div class="abs job-date" style="left:478px;top:1297px">2012-2013</div>

<div class="abs job-card" style="left:163px;top:1448px"><div class="job-title">Brightsmith Labs</div><div class="job-role">Assistant Graphic designer</div></div>
<div class="abs timeline-node" style="left:570px;top:1457px"><svg width="22" height="22" viewBox="0 0 22 22"><path d="M4 18 L16 6 M4 4 L18 18" stroke="#111" stroke-width="3"/><rect x="13" y="2" width="7" height="5" fill="#111" transform="rotate(45 16 4)"/></svg></div>
<div class="abs job-date" style="left:634px;top:1470px">2010-2012</div>

<div class="abs job-card" style="left:648px;top:1625px"><div class="job-title">Tolvane Media</div><div class="job-role">Trainee web &amp; Graphic designer</div></div>
<div class="abs timeline-node" style="left:570px;top:1634px"><svg width="22" height="22" viewBox="0 0 22 22"><path d="M4 18 L16 6 M4 4 L18 18" stroke="#111" stroke-width="3"/><rect x="13" y="2" width="7" height="5" fill="#111" transform="rotate(45 16 4)"/></svg></div>
<div class="abs job-date" style="left:478px;top:1647px">2006-2009</div>

<h2 class="abs section-title" style="top:1854px">Software I love</h2>
<div class="abs tool" style="left:376px;top:1945px">Flintmoor</div>
<div class="abs tool" style="left:494px;top:1945px">Dewmarq</div>
<div class="abs tool" style="left:612px;top:1945px">Aildra</div>
<div class="abs tool" style="left:730px;top:1945px">Pixvane</div>

<section class="abs band" style="top:2087px;height:607px"></section>
<h2 class="abs section-title" style="top:2114px">Latest Work</h2>

<div class="abs work-shot" style="left:0;top:2240px;width:365px;height:168px;background:linear-gradient(180deg,#2b2b2b 0 14%,#e9e9e9 14% 55%,#c7262b 55% 62%,#f4f4f4 62%)" role="img" aria-label="Website screenshot for an online store with red accents"><span class="work-tag">Plenvora</span></div>
<div class="abs work-shot" style="left:0;top:2421px;width:365px;height:254px;background:linear-gradient(135deg,#d9b39a,#b07a6a 50%,#6b4a4a)" role="img" aria-label="Beauty website screenshot with model portraits"><span class="work-tag">Bellamire</span></div>

<div class="abs work-card" style="left:398px;top:2240px;width:405px;height:252px">
  <div class="work-card-title">Plenvora</div>
  <div class="work-card-meta">Category: <span>web design</span></div>
  <div class="abs" style="left:319px;top:0;width:86px;height:160px;background:linear-gradient(180deg,#8a7a6a,#d9d4cc)" role="img" aria-label="Website preview thumbnail"></div>
  <div class="work-details">DETAILS</div>
</div>
<div class="abs work-shot" style="left:398px;top:2509px;width:405px;height:166px;background:linear-gradient(135deg,#f0287f,var(--pink))" role="img" aria-label="Pink app landing page with a phone mockup"><span class="work-tag" style="background:#c40f66">Yuvella</span></div>

<div class="abs work-shot" style="left:833px;top:2240px;width:367px;height:174px;background:linear-gradient(180deg,#1d1d1d 0 12%,#9a8a5c 12%,#5a6a3a 70%,#3a3f2a)" role="img" aria-label="Website screenshot with a hiker in a field landscape"><span class="work-tag">Shopwick Corner</span></div>
<div class="abs work-shot" style="left:833px;top:2430px;width:367px;height:245px;background:linear-gradient(180deg,#222 0 10%,#f6f6f6 10% 70%,#e8e8e8 70%)" role="img" aria-label="Electronics store website screenshot with washing machines"><span class="work-tag">Makrizo</span></div>

<h2 class="abs section-title" style="top:2731px">Contacts</h2>
<p class="abs contact-line" style="top:2820px">You can write me an e-mail...</p>
<div class="abs email-pill">hello@rayanmalik.design</div>
<p class="abs contact-line" style="top:2952px">... and you can find me on the social!</p>
<div class="abs social" style="left:345px;top:3034px">Chatterly</div>
<div class="abs social" style="left:479px;top:3034px">Wrenzo</div>
<div class="abs social" style="left:615px;top:3034px">Talvine</div>
<div class="abs social" style="left:751px;top:3034px;background:#555">Orbelle</div>

<footer class="abs footer-strip">Scroll to top</footer>

</body>
</html>
```